KVR bottled water label

We are from The KVR Shop (TKS) - a university campus-retail initiative. As part of our branding exercise, we would like to produce a new range of bottled water and need a new label design carrying the following headline: "U Make A Different U" (primary headline) with "The World Is Your Campus" as the sub-headline (secondary headline).
Usage Of Line:
Emphasis must be given to the primary headline, and must not be placed before or on top of the primary headline. The reader must first read the primary headline before reading the secondary headline (assuming the reader reads from left to right and top to bottom.)
THE CONCEPT BEHIND OUR LINE:
Some Background:
Perceived as a fast-rising star since our inception in 2000, Harbourline Civic University challenged the Singapore education landscape - long dominated by an established field of long-tenured universities – by providing a holistic, broad-based and cross-disciplinary form of education that incorporates global exposure, internships and networking opportunities to prepare our students for real-world challenges - an experiential learning environment which we’ve proudly pioneered. Watch these videos from our graduates sharing their KVR experiences: http://kvr.example/22
When our first batch of graduates started their careers in 2004, employers saw a different breed of leaders. The graduates from KVR were bold, confident, articulate, versatile, well-rounded and eager for challenges. Today, more than 10,000 graduates across the world are testament to our trademark holistic and interactive approach to education. Our graduate employment record has been, and continues to be, robust with 60% finding jobs before graduation, and close to 100% getting employed within six months of graduation. Watch employers from Zentrova, QHL, WEV & LNJ at: http://kvr.example/21
That is why we invite prospective students to Discover A Different 'U' - the letter 'U' can be interpreted to mean the 'U'niversity or 'U' as an individual (the prospective student).
The New Line:
With our new headline "U Make A Different U - The World Is Your Campus", we now pose the challenge back to our prospective students, and invite them to make a difference. How different their university experience can be, and how much they can be transformed, is limited only by their imagination.
For more information on KVR, please visit our website at: kvr.example.edu
Design:
The design must be vibrant and fresh to appeal to our students (from 18 years of age), yet still fit in perfectly on a table for a board of professionals and executive directors.
Audience:
It should appeal to the general masses, from our students to distinguished guests and executive directors to KVR.
Things to include (Requirements):
1. KVR logo (as below) must be included)
https://files.example.net/s/qk41tm8rb2xw/KVR%20Formal%20Logo.zip
2. Only 4 colours can be used (white is considered one color)
3. Must design within perimeters of working file:
https://files.example.net/s/hp73nd5ye9ja/bottled%20water%20working%20file.pdf
References
http://kvr.example/1m
http://kvr.example/1o
http://kvr.example/1p
http://kvr.example/1q
http://kvr.example/1r
http://kvr.example/1s
http://kvr.example/1t
http://kvr.example/1u
http://kvr.example/1v
http://kvr.example/1w
http://kvr.example/1x
http://kvr.example/1y

```html
<!DOCTYPE html>
<html lang="en">
<head>
<meta charset="utf-8">
<title>KVR Bottled Water Label</title>
<link href="https://fonts.googleapis.com/css2?family=Audiowide&family=Great+Vibes&family=Arimo:wght@400;700&display=swap" rel="stylesheet">
<style>
  :root {
    --teal-deep: #125a70;
    --teal-mid: #2b8ea7;
    --teal-light: #5cc0d4;
    --navy: #1b2a5e;
    --white: #ffffff;
    --ink: #1a1a1a;
  }
  * { box-sizing: border-box; margin: 0; padding: 0; }
  html, body { width: 1200px; height: 237px; overflow: hidden; background: var(--white); }
  .label {
    position: relative;
    width: 1200px;
    height: 237px;
    overflow: hidden;
    background: linear-gradient(90deg, var(--teal-deep) 0%, var(--teal-mid) 30%, var(--teal-light) 55%, var(--teal-mid) 80%, var(--teal-deep) 100%);
  }
  .label__band {
    position: absolute; left: 0; right: 0; height: 6px; background: var(--navy); opacity: .35;
  }
  .label__band--top { top: 0; }
  .label__band--bottom { bottom: 0; }
  .hair-illustration {
    position: absolute; left: 0; top: 0; width: 415px; height: 237px;
    background: radial-gradient(ellipse at 40% 55%, #e8f5f8 0%, #9fd3df 35%, rgba(43,142,167,0) 75%);
  }
  .swirl-ornament {
    position: absolute; left: 760px; top: 0; width: 190px; height: 237px;
    background: radial-gradient(ellipse at 40% 50%, rgba(255,255,255,.4) 0%, rgba(255,255,255,0) 70%);
  }
  .brand {
    position: absolute; left: 500px; top: 16px;
    display: flex; align-items: center; gap: 8px;
    color: var(--navy);
    font-family: "Audiowide", sans-serif;
  }
  .brand__mark { width: 18px; height: 18px; background: var(--navy); }
  .brand__name { font-size: 24px; line-height: 1; display: block; }
  .brand__full { font-size: 7px; letter-spacing: .5px; display: block; margin-top: 2px; }
  .headline {
    position: absolute; left: 380px; top: 76px; width: 500px;
    text-align: center;
    white-space: nowrap;
    font-family: "Audiowide", sans-serif;
    font-weight: 400;
    font-size: 29px; line-height: 1;
    color: var(--white);
    letter-spacing: .5px;
    text-transform: uppercase;
  }
  .subheadline {
    position: absolute; left: 380px; top: 110px; width: 500px;
    text-align: center;
    white-space: nowrap;
    font-family: "Great Vibes", cursive;
    font-size: 36px; line-height: 1.1;
    color: var(--white);
  }
  .info-panel {
    position: absolute; left: 948px; top: 4px; width: 248px; height: 229px;
    background: var(--white);
    padding: 5px 8px;
    font-family: "Arimo", sans-serif;
    color: var(--ink);
  }
  .info-panel__product { font-size: 11px; font-weight: 700; text-align: center; margin-bottom: 3px; }
  .nutrition { width: 100%; border: 1px solid var(--ink); border-collapse: collapse; font-size: 7px; }
  .nutrition caption { font-size: 9px; font-weight: 700; text-align: left; border: 1px solid var(--ink); border-bottom: 0; padding: 1px 3px; }
  .nutrition td, .nutrition th { padding: 0 3px; text-align: left; font-weight: 400; }
  .nutrition .num { text-align: right; }
  .nutrition tr.rule td, .nutrition tr.rule th { border-top: 1px solid var(--ink); }
  .fine-print { font-size: 6.5px; line-height: 1.35; margin-top: 3px; }
  .producer { margin-top: 5px; font-size: 8px; font-weight: 700; }
  .producer__name { font-size: 20px; font-weight: 700; line-height: 1; margin-top: 2px; }
  .producer__name small { font-size: 8px; font-weight: 400; }
</style>
</head>
<body>
<main class="label">
  <div class="label__band label__band--top"></div>
  <div class="label__band label__band--bottom"></div>

  <div class="hair-illustration" role="img" aria-label="Illustration of a woman's silhouette with flowing swirling hair"></div>
  <div class="swirl-ornament" role="img" aria-label="Decorative white swirls"></div>

  <div class="brand">
    <span class="brand__mark"></span>
    <span>
      <span class="brand__name">KVR</span>
      <span class="brand__full">HARBOURLINE CIVIC UNIVERSITY</span>
    </span>
  </div>

  <h1 class="headline">U Make A Different U</h1>
  <p class="subheadline">The World Is Your Campus</p>

  <aside class="info-panel">
    <p class="info-panel__product">Oxygenated Drinking Water</p>
    <table class="nutrition">
      <caption>Nutrition Information</caption>
      <tr class="rule"><td colspan="3">Serving per package: 300ml</td></tr>
      <tr><td colspan="3">Serving size: 100ml</td></tr>
      <tr class="rule"><th></th><th class="num">per serving</th><th class="num">per 100ml</th></tr>
      <tr class="rule"><td>energy</td><td class="num">0 kcal*</td><td class="num">0 kcal*</td></tr>
      <tr><td>protein</td><td class="num">0 g</td><td class="num">0 g</td></tr>
      <tr><td>total fat</td><td class="num">0 g</td><td class="num">0 g</td></tr>
      <tr><td>carbohydrate</td><td class="num">0 g</td><td class="num">0 g</td></tr>
      <tr><td>sodium</td><td class="num">0 g</td><td class="num">0 g</td></tr>
    </table>
    <p class="fine-print">
      *1 kcal = 4.2kJ<br>
      Not a significant source of dietary fibre, saturated fats and cholesterol.<br>
      Manufactured in Singapore by:<br>
      AQUALIS GLOBAL WATERTECH (S) PTE LTD<br>
      TEL: +65 6000 0000 &nbsp; FAX: +65 6000 0001<br>
      EMAIL: hello@aqualis.example
    </p>
    <p class="producer">Produced Using The Technology of</p>
    <p class="producer__name">DR.AQUALIS <small>Singapore</small></p>
  </aside>
</main>
</body>
</html>
```